WordPress Theme for "lxt graz" the large largest offically Recognized wine competition in the world

Our company "lxt graz" carries out the large largest offically Recognized wine competition in the world. We would like to redesign our existing website (www.lxt-fernhold.example). We use Drupal at the moment, but would like to move to WordPress. The site is in German and English (switchable). Following importent elements shoulderstand be in the design: - A timeline layout for awc year (example: https://www.lxt-fernhold.example/en/home at the bottom of the page). - Layout Elemenst for awards stars (example: https://www.lxt-fernhold.example/en/auszeichnungen at "Stars Winery"). - Layout for picture gallery - and all other elements of the origin site - ... footer content must be adjustable (example: https://www.lxt-fernhold.example/en/home at the bottom of the page). The wordpress theme must be adjustable (default colors, head pictures, partner logos, ...). The corporate design shoulderstand Be The Same Final result shoulderstand be a ready to use responsive WordPress theme. New ideas are welcome.

```html
<!DOCTYPE html>
<html lang="en">
<head>
<meta charset="utf-8">
<title>Lxt Graz – International Wine Competition</title>
<link rel="stylesheet" href="https://fonts.googleapis.com/css2?family=Roboto:wght@300;400;500;700&family=Roboto+Slab:wght@300;400&display=swap">
<style>
:root{
  --green:#4ba545;
  --green-dark:#3f9139;
  --ink:#2b2b2b;
  --text:#333333;
  --muted:#666666;
  --header:#2a2a2a;
  --grey-bg:#f4f5f7;
  --footer-bg:#f3f3f3;
  --bottom:#2b2b2b;
  --white:#ffffff;
  --line:#e2e2e2;
}
*{box-sizing:border-box;margin:0;padding:0}
html,body{width:1200px;height:3020px;overflow:hidden}
body{font-family:"Roboto",Arial,sans-serif;color:var(--text);background:var(--white);position:relative;font-size:13px;line-height:1.55}
.abs{position:absolute}
.slab{font-family:"Roboto Slab",Georgia,serif;font-weight:400}

/* header */
.site-header{position:absolute;left:0;top:0;width:1200px;height:110px;background:var(--header)}
.brand{position:absolute;left:110px;top:30px;color:var(--white);font-family:"Roboto",Arial,sans-serif;font-weight:300;font-size:40px;letter-spacing:3px;line-height:50px;display:flex;align-items:center;gap:14px}
.brand-square{width:14px;height:14px;background:var(--green)}
.lang{position:absolute;top:38px;height:38px;display:flex;align-items:center;gap:10px;padding:0 14px;font-size:13px;color:#ddd;border-radius:3px}
.lang.en{left:908px;background:var(--green);color:var(--white)}
.lang.de{left:1012px;background:#343434}
.flag{width:20px;height:13px;display:inline-block}
.flag.uk{background:#1f3f8c;border:2px solid #fff;box-shadow:inset 0 0 0 3px #c8202f}
.flag.deu{background:linear-gradient(#111 33%,#d00 33% 66%,#fc0 66%)}

.main-nav{position:absolute;left:0;top:110px;width:1200px;height:60px;background:var(--green);border-bottom:2px solid var(--green-dark)}
.main-nav a{position:absolute;top:0;line-height:58px;color:var(--white);text-decoration:none;font-size:15px;font-weight:500;transform:translateX(-50%)}

/* hero */
.hero{position:absolute;left:0;top:170px;width:1200px;height:505px}
.hero-photo{position:absolute;inset:0;background:
 radial-gradient(ellipse 380px 340px at 640px 190px,rgba(150,120,50,.55),transparent 70%),
 radial-gradient(ellipse 300px 420px at 970px 300px,rgba(220,200,140,.55),transparent 70%),
 linear-gradient(90deg,#100d08 0%,#2a2114 35%,#4b3c22 60%,#2a2116 100%)}
.hero h1{position:absolute;left:86px;top:118px;color:var(--white);font-weight:300;font-size:60px;line-height:1.1}
.hero h2{position:absolute;left:86px;top:200px;color:#6cc35f;font-weight:400;font-size:26px}
.hero p{position:absolute;left:86px;top:246px;width:850px;color:#f2f2f2;font-size:13.5px;line-height:1.75}
.btn{position:absolute;left:86px;top:343px;width:151px;height:47px;background:var(--green);color:var(--white);font-size:15px;font-weight:500;text-align:center;line-height:47px;border-radius:3px}
.dots{position:absolute;left:560px;top:468px;display:flex;gap:5px}
.dots span{width:15px;height:15px;border:2px solid #ddd;border-radius:50%}

/* intro columns */
.intro{position:absolute;left:0;top:675px;width:1200px;height:398px;background:var(--white)}
.col{position:absolute;top:50px}
.col h3{font-family:"Roboto Slab",Georgia,serif;font-weight:400;color:var(--green);font-size:21px;line-height:1.3;margin-bottom:14px}
.col h4{font-family:"Roboto Slab",Georgia,serif;font-weight:400;color:var(--ink);font-size:17px;line-height:1.55;margin-bottom:14px}
.col p{font-size:12.5px;line-height:1.75;color:var(--text);margin-bottom:14px}
.medal-img{position:absolute;left:6px;top:48px;width:115px;height:107px;background:radial-gradient(circle at 50% 45%,#d8b552,#8a7446 55%,#6e6e6e);border:4px solid #eee}
.medal-text{position:absolute;left:139px;top:44px;width:205px;font-size:12.5px;line-height:1.75}
.file-link{display:flex;align-items:center;gap:10px;font-size:12.5px;line-height:28px;color:var(--text)}
.pdf{width:12px;height:14px;background:#d23a2f;clip-path:polygon(0 0,70% 0,100% 28%,100% 100%,0 100%)}

/* trophy */
.trophy{position:absolute;left:0;top:1073px;width:1200px;height:473px;background:var(--grey-bg)}
.certificate{position:absolute;left:117px;top:38px;width:306px;height:393px;background:#111;padding:10px}
.certificate div{width:100%;height:100%;background:linear-gradient(180deg,#f6f6f3 0%,#ebe7df 45%,#f4f4f2 100%)}
.trophy h3{position:absolute;left:445px;top:38px;color:var(--green);font-size:20px;font-weight:500}
.trophy-list{position:absolute;left:445px;top:86px;width:440px;list-style:none}
.trophy-list li{position:relative;height:36.5px;line-height:36.5px;border-bottom:1px solid var(--line);padding-left:38px;font-size:13px}
.trophy-list li svg{position:absolute;left:4px;top:12px}
.trophy-list .amt{position:absolute;right:0;top:0}
.trophy h5{position:absolute;left:445px;top:288px;color:var(--green);font-size:14px;font-weight:500}
.trophy p{position:absolute;left:445px;top:318px;width:600px;font-size:12.5px;line-height:1.9}
.store{position:absolute;top:386px;width:100px;height:31px;border-radius:4px}
.store.a{left:445px;background:#111}
.store.b{left:552px;background:#9ccf4a}

/* timeline */
.timeline{position:absolute;left:0;top:1546px;width:1200px;height:467px;background:var(--white)}
.section-title{position:absolute;left:0;width:1200px;text-align:center;font-family:"Roboto Slab",Georgia,serif;font-weight:400;color:var(--green);font-size:31px}
.section-sub{position:absolute;left:0;width:1200px;text-align:center;font-size:12.5px;color:var(--text)}
.tl-bar{position:absolute;left:0;top:256px}
.ev{position:absolute;font-size:12px;line-height:20px;color:var(--text)}
.ev b{display:block;color:var(--green);font-weight:500;font-size:12.5px}
.ev.right{text-align:left}
.pin{position:absolute;width:9px;height:9px;border-radius:50%;background:var(--green)}
.dash{position:absolute;width:0;border-left:2px dashed #9a9a9a}

/* gallery */
.gallery{position:absolute;left:0;top:2013px;width:1200px;height:392px;background:var(--grey-bg)}
.photo{position:absolute;top:127px;width:252px;height:211px}

/* partners */
.partners{position:absolute;left:0;top:2405px;width:1200px;height:280px;background:var(--white);border-bottom:4px solid var(--green)}
.partner{position:absolute;top:127px;width:177px;height:99px;border:1px solid #e6e6e6;padding:12px}
.partner div{width:100%;height:100%;background:#dcdcdc}
.arrow{position:absolute;top:150px}

/* footer */
.site-footer{position:absolute;left:0;top:2687px;width:1200px;height:262px;background:var(--footer-bg)}
.fcol{position:absolute;top:42px}
.fcol h6{font-size:15px;font-weight:700;color:var(--ink);letter-spacing:.5px;margin-bottom:16px}
.fcol ul{list-style:none}
.fcol li{font-size:12px;line-height:25.5px;color:var(--text);position:relative;padding-left:22px}
.fcol li::before{content:"";position:absolute;left:2px;top:9px;border-left:6px solid #444;border-top:4px solid transparent;border-bottom:4px solid transparent}
.cards{display:flex;gap:4px}
.cards span{width:40px;height:27px;border-radius:3px;border:1px solid #ccc}
.social{display:flex;gap:8px;margin-top:22px}
.social span{width:33px;height:33px;border:1.5px solid #8a8a8a;border-radius:50%}
.contact li{padding-left:28px;font-size:12px;line-height:19px;margin-bottom:13px}
.contact li::before{display:none}
.contact svg{position:absolute;left:0;top:3px}
.contact .mail{text-decoration:underline}
.bottom-bar{position:absolute;left:0;top:2949px;width:1200px;height:71px;background:var(--bottom);color:#e8e8e8;font-size:12px;text-align:center;line-height:71px}
.bottom-bar .tag{position:absolute;right:52px;top:0;font-size:12px}
</style>
</head>
<body>

<header class="site-header">
  <div class="brand"><span class="brand-square"></span>LXT GRAZ</div>
  <div class="lang en"><span class="flag uk"></span>English</div>
  <div class="lang de"><span class="flag deu"></span>German</div>
</header>

<nav class="main-nav">
  <a style="left:165px">HOME</a>
  <a style="left:286px">CURRENT</a>
  <a style="left:437px">LXT GRAZ</a>
  <a style="left:578px">AWARDS</a>
  <a style="left:700px">SUBMIT</a>
  <a style="left:837px">DOWNLOADS</a>
  <a style="left:1000px">SUBMIT LOGIN</a>
</nav>

<section class="hero">
  <div class="hero-photo" role="img" aria-label="White wine being poured into glasses against a warm, dark background"></div>
  <h1>Lxt-Graz</h1>
  <h2>Lxt Graz Whitebook App 2016 Update!</h2>
  <p>The lxt graz 2016 exceeds all expectations again &amp; impressively confirms the leading role among the officially recognized quality awards. Never before have so many wines been compared to the international market.</p>
  <div class="btn">READ MORE</div>
  <div class="dots"><span></span><span></span><span></span><span></span></div>
</section>

<section class="intro">
  <div class="col" style="left:86px;width:330px">
    <h3>12,826 Wines From 1,866 Producers</h3>
    <h4>From 41 countries face the international comparison &nbsp;a new world record!</h4>
    <p>The lxt graz 2016 exceeds all expectations again &amp; impressively confirms the leading role among the officially recognized quality awards. Never before have so many wines been compared to the international market.</p>
    <p>The leading role among the officially recognized quality award Never before have so many wines been compared to the international market.</p>
  </div>
  <div class="col" style="left:479px;width:330px;height:330px">
    <h3>Order Of Medals</h3>
    <div class="medal-img" role="img" aria-label="Gold and silver medal bottle stickers"></div>
    <div class="medal-text">The lxt graz 2016 exceed all expectations again &amp; impressively confirms the leading role among the officially recognized quality awards.</div>
    <div style="position:absolute;top:172px;width:300px">
      <p style="margin-bottom:6px">Original dimensions of bottle stickers: 35mm adhesive self &nbsp;on rolls of 1,000 pcs.</p>
      <div class="file-link"><span class="pdf"></span>Order form Medaillen 2016</div>
      <div class="file-link"><span class="pdf"></span>PDF icon Order form medals 2016</div>
    </div>
  </div>
  <div class="col" style="left:825px;width:300px">
    <h3>Lxt Graz Media Package</h3>
    <h4>Everything with just one download!</h4>
    <p>For your advertising and communication activities,the lxt graz media package offers all lxt graz printing presses - logo, medals, pictures, folders, APP, press texts, etc. - high-resolution (print) and low-resolution (web).</p>
    <div class="file-link"><span class="pdf"></span>Lxt Graz Media Package '16 (~ 13 Mb)</div>
    <div class="file-link" style="margin-top:8px"><span class="pdf"></span>Pdf Icon Order Form Medaillen 2016</div>
  </div>
</section>

<section class="trophy">
  <div class="certificate"><div role="img" aria-label="Framed gold award certificate with a grape illustration"></div></div>
  <h3>LXT GRAZ TROPHY WINNERS 2016</h3>
  <ul class="trophy-list">
    <li><svg width="14" height="12" viewBox="0 0 14 12"><path d="M1 6l4 4 8-9" fill="none" stroke="#4ba545" stroke-width="2.4"/></svg>Lxt graz 2016 offers a prize money in total value of<span class="amt">€ 8.000</span></li>
    <li><svg width="14" height="12" viewBox="0 0 14 12"><path d="M1 6l4 4 8-9" fill="none" stroke="#4ba545" stroke-width="2.4"/></svg>Best white wine of the year 2016<span class="amt">€ 2.000</span></li>
    <li><svg width="14" height="12" viewBox="0 0 14 12"><path d="M1 6l4 4 8-9" fill="none" stroke="#4ba545" stroke-width="2.4"/></svg>Best red wine of the year 2016<span class="amt">€ 2.000</span></li>
    <li><svg width="14" height="12" viewBox="0 0 14 12"><path d="M1 6l4 4 8-9" fill="none" stroke="#4ba545" stroke-width="2.4"/></svg>Best sweet wine of the year 2016<span class="amt">€ 2.000</span></li>
    <li><svg width="14" height="12" viewBox="0 0 14 12"><path d="M1 6l4 4 8-9" fill="none" stroke="#4ba545" stroke-width="2.4"/></svg>Best sparkling wine of the year 2016<span class="amt">€ 2.000</span></li>
  </ul>
  <h5>LXT GRAZ TROPHIES 2016</h5>
  <p>The award for the best wine of each tasting category.At the master tasting, which is a commissional, parallel blind tasting, the wines will be ranked from 1. to 6. The primary-ranked wine of each tasting category achieves</p>
  <div class="store a"></div>
  <div class="store b"></div>
</section>

<section class="timeline">
  <h2 class="section-title" style="top:38px">Timetable 2017</h2>

  <div class="dash" style="left:130px;top:124px;height:132px"></div>
  <div class="pin" style="left:126px;top:110px"></div>
  <div class="ev" style="left:145px;top:102px"><b>REGISTRATION PERIOD OF TASTINGS</b>10 April to 1 May 2017</div>

  <div class="dash" style="left:441px;top:140px;height:116px"></div>
  <div class="pin" style="left:437px;top:127px"></div>
  <div class="ev" style="left:461px;top:122px"><b>LXT GRAZ LOGISTICS CENTER</b>Control &amp; Sorting<br>of about 40,000 wine bottles</div>

  <div class="dash" style="left:1069px;top:124px;height:132px"></div>
  <div class="pin" style="left:1065px;top:110px"></div>
  <div class="ev" style="left:890px;top:102px"><b>DISPATCH OF DOCUMENTS</b>&nbsp;late October</div>
  <div class="ev" style="left:888px;top:160px"><b>LXT GRAZ GALA NIGHT<br>OF WINE 2017</b>end of October</div>

  <svg class="tl-bar" width="1200" height="46" viewBox="0 0 1200 46">
    <g fill="#4ba545">
      <polygon points="46,0 194,0 210,46 62,46"/>
      <polygon points="204,0 352,0 368,46 220,46"/>
      <polygon points="362,0 510,0 526,46 378,46"/>
      <polygon points="520,0 668,0 684,46 536,46"/>
      <polygon points="678,0 826,0 842,46 694,46"/>
      <polygon points="836,0 984,0 1000,46 852,46"/>
      <polygon points="994,0 1138,0 1154,46 1010,46"/>
    </g>
    <g fill="#fff" font-family="Roboto Slab, Georgia, serif" font-size="17" font-weight="700" text-anchor="middle">
      <text x="128" y="29">APRIL</text>
      <text x="286" y="29">MAY</text>
      <text x="444" y="29">JUNE</text>
      <text x="602" y="29">JULY</text>
      <text x="760" y="29">AUGUST</text>
      <text x="918" y="29">SEPTEMBER</text>
      <text x="1074" y="29">OCTOBER</text>
    </g>
  </svg>

  <div class="dash" style="left:292px;top:302px;height:78px"></div>
  <div class="pin" style="left:288px;top:375px"></div>
  <div class="ev" style="left:306px;top:366px"><b>SUBMISSION PERIOD OF TASTINGS</b>02 May to 24 May 2017</div>

  <div class="dash" style="left:741px;top:302px;height:62px"></div>
  <div class="pin" style="left:737px;top:360px"></div>
  <div class="ev" style="left:624px;top:340px"><b>TASTING THE<br>WINE TASTING</b>by the jury &nbsp;August 2017</div>

  <div class="dash" style="left:918px;top:302px;height:88px"></div>
  <div class="pin" style="left:914px;top:386px"></div>
  <div class="ev" style="left:934px;top:378px"><b>MASTER TASTING IN 2017</b>in early September 2017</div>
</section>

<section class="gallery">
  <h2 class="section-title" style="top:36px">Photo Gallery</h2>
  <p class="section-sub" style="top:80px">For your advertising and communication activities, the lxt graz media package offers all lxt graz printing presses</p>
  <div class="photo" style="left:86px;background:linear-gradient(160deg,#6b5a45,#c8a77c 50%,#4d3b2a)" role="img" aria-label="Guests at a wine tasting table"></div>
  <div class="photo" style="left:344px;background:linear-gradient(150deg,#1e1412,#7a1a1c 45%,#c9c2bb)" role="img" aria-label="Red wine poured from a bottle into a glass"></div>
  <div class="photo" style="left:604px;background:linear-gradient(180deg,#8fa47a,#4e6a3a 50%,#3a2f35)" role="img" aria-label="Vineyard rows with dark grape bunches"></div>
  <div class="photo" style="left:862px;background:linear-gradient(170deg,#2a2420,#6d5c4c 50%,#d8d2ca)" role="img" aria-label="Wine bottles lying stacked in a cellar rack"></div>
</section>

<section class="partners">
  <h2 class="section-title" style="top:30px">Our Partners</h2>
  <p class="section-sub" style="top:76px">For your advertising and communication activities, the lxt graz media package offers all lxt graz printing presses</p>
  <svg class="arrow" style="left:48px" width="16" height="60" viewBox="0 0 16 60"><path d="M14 2L2 30l12 28" fill="none" stroke="#ddd" stroke-width="2"/></svg>
  <div class="partner" style="left:107px"><div></div></div>
  <div class="partner" style="left:306px"><div></div></div>
  <div class="partner" style="left:510px"><div></div></div>
  <div class="partner" style="left:713px"><div></div></div>
  <div class="partner" style="left:920px"><div></div></div>
  <svg class="arrow" style="left:1136px" width="16" height="60" viewBox="0 0 16 60"><path d="M2 2l12 28L2 58" fill="none" stroke="#ddd" stroke-width="2"/></svg>
</section>

<footer class="site-footer">
  <div class="fcol" style="left:93px">
    <h6>PAYMENTS ACCEPTED</h6>
    <div class="cards"><span style="background:#e8ecf4"></span><span style="background:#f4ebe2"></span><span style="background:#e6eef4"></span><span style="background:#f3efe6"></span></div>
    <div class="social"><span></span><span></span><span></span><span></span><span></span></div>
  </div>
  <div class="fcol" style="left:318px">
    <h6>LXT GRAZ</h6>
    <ul><li>Introduction</li><li>Your lxt graz bonus</li><li>The tasting</li><li>Lxt graz Gala Night</li><li>Just 2 steps &nbsp;your submission</li><li>Lxt graz bonus</li></ul>
  </div>
  <div class="fcol" style="left:540px">
    <h6>AWARDS</h6>
    <ul><li>Trophies</li><li>Star winery rating</li><li>Lxt graz special awards</li><li>Medals</li><li>Information &amp; Downloads</li></ul>
  </div>
  <div class="fcol" style="left:747px">
    <h6>SUBMIT</h6>
    <ul><li>Just 2 steps to your</li><li>Lxt graz bonus</li><li>Events 2017</li><li>Information &amp; Downloads</li><li>Lxt graz Whitebook</li></ul>
  </div>
  <div class="fcol contact" style="left:938px">
    <h6>CONTACT US</h6>
    <ul>
      <li><svg width="14" height="12" viewBox="0 0 14 12"><path d="M1 3c0-2 12-2 12 0v2h-3V3.5H4V5H1z M3 6h8l1 5H2z" fill="#444"/></svg>+43 / 316 / 55 01 200 (Phone)</li>
      <li><svg width="14" height="12" viewBox="0 0 14 12"><rect x="3" y="0" width="8" height="4" fill="#444"/><rect x="0" y="4" width="14" height="6" rx="1" fill="#444"/><rect x="3" y="8" width="8" height="4" fill="#777"/></svg>+43 / 316 / 55 01 209 &nbsp;&nbsp;&nbsp;(Fax)</li>
      <li><svg width="14" height="12" viewBox="0 0 14 12"><rect x="0.5" y="1.5" width="13" height="9" fill="none" stroke="#444"/><path d="M1 2l6 5 6-5" fill="none" stroke="#444"/></svg><span class="mail">office@lxt-fernhold.example</span></li>
      <li><svg width="12" height="14" viewBox="0 0 12 14"><path d="M6 0a5 5 0 0 1 5 5c0 4-5 9-5 9S1 9 1 5a5 5 0 0 1 5-5z" fill="#444"/><circle cx="6" cy="5" r="2" fill="#f3f3f3"/></svg>Fernholdgasse 12 8010 Graz<br>Austria, Europe</li>
    </ul>
  </div>
</footer>

<div class="bottom-bar">© Copyright 2017 Lxt-Graz.All Rights Reserved<span class="tag">C2</span></div>

</body>
</html>
```